Veteran Reserved Parking Sign 12x18

Steadfast Homefront Kin Alliance is looking to have a new Veteran Reserved Parking Sign designed. Included in the files are our current logo, the rectangle with the name on it. Also included is our Alt Square version that we will often use. There are several other signs that we kind of like as examples, not not asking for exactly like those, we want you to be creative and show us some new ideas. These are full sized parking signs, 12" wide X 18" height.

Target Market(s)

Veterans and Military Friendly Americans

Industry/Entity Type

Veteran Nonprofit

Font styles to use
Other font styles liked:
• Our logo uses the Franklin Heavy Gothic Font but you are not required to use that font in design.

Requirements
Must have
• Our logo needs to be on there and well as SHKA.ORG
Should not have
• CAN NOT Mention Brave Return Initiative or have black silhouettes similar to their logo. SHKA is NOT the same nonprofit.

```html
<!DOCTYPE html>
<html lang="en">
<head>
<meta charset="utf-8">
<title>SHKA Veteran Reserved Parking Sign</title>
<link href="https://fonts.googleapis.com/css2?family=Roboto+Slab:wght@900&family=Oswald:wght@400&display=swap" rel="stylesheet">
<style>
  :root {
    --backdrop: #221f1f;
    --navy: #0d3165;
    --crimson: #b71a45;
    --white: #ffffff;
    --flag-red: #c8303f;
    --flag-blue: #28407e;
    --flag-white: #e9eef6;
  }
  html, body {
    margin: 0;
    padding: 0;
    width: 1200px;
    height: 1200px;
    overflow: hidden;
    background: var(--backdrop);
  }
  .sign {
    position: absolute;
    left: 248px;
    top: 72px;
    width: 704px;
    height: 1055px;
    background: var(--navy);
    overflow: hidden;
  }
  .sign-art {
    position: absolute;
    left: 0;
    top: 0;
    width: 704px;
    height: 520px;
  }
  .badge-name {
    position: absolute;
    left: 40px;
    top: 240px;
    width: 284px;
    text-align: center;
    font-family: "Roboto Slab", serif;
    font-weight: 900;
    font-size: 62px;
    line-height: 62px;
    color: var(--crimson);
  }
  .headline {
    position: absolute;
    left: 51px;
    margin: 0;
    font-family: "Roboto Slab", serif;
    font-weight: 900;
    font-size: 104px;
    line-height: 1;
    letter-spacing: 1px;
    white-space: nowrap;
  }
  .headline--veteran { top: 517px; color: var(--white); }
  .headline--reserved { top: 613px; color: var(--crimson); }
  .headline--parking { top: 709px; color: var(--white); }
  .web-band {
    position: absolute;
    left: 56px;
    top: 844px;
    width: 648px;
    height: 77px;
    background: var(--crimson);
    border-radius: 13px 0 0 13px;
  }
  .web-band__address {
    position: absolute;
    left: 22px;
    top: 9px;
    font-family: "Roboto Slab", serif;
    font-weight: 900;
    font-size: 52px;
    line-height: 1;
    letter-spacing: 1px;
    color: var(--white);
  }
  .thanks {
    position: absolute;
    left: 56px;
    top: 974px;
    margin: 0;
    font-family: "Oswald", sans-serif;
    font-weight: 400;
    font-size: 46px;
    line-height: 1;
    letter-spacing: -1.5px;
    color: var(--white);
    white-space: nowrap;
  }
</style>
</head>
<body>
  <main class="sign">
    <svg class="sign-art" viewBox="0 0 704 520" xmlns="http://www.w3.org/2000/svg">
      <defs>
        <linearGradient id="flagTones" x1="0" y1="0" x2="1" y2="1">
          <stop offset="0" stop-color="var(--flag-blue)"/>
          <stop offset="0.42" stop-color="var(--flag-blue)"/>
          <stop offset="0.55" stop-color="var(--flag-white)"/>
          <stop offset="0.75" stop-color="var(--flag-red)"/>
          <stop offset="1" stop-color="var(--flag-red)"/>
        </linearGradient>
      </defs>
      <circle class="flag-ring" cx="491" cy="121" r="318" fill="var(--white)"/>
      <circle class="flag-ring-gap" cx="491" cy="121" r="315" fill="var(--navy)"/>
      <circle class="flag-photo" cx="491" cy="121" r="311" fill="url(#flagTones)" role="img" aria-label="Photograph of a waving American flag"/>
      <circle class="badge-disc" cx="182" cy="271" r="143" fill="var(--white)"/>
      <circle class="badge-line" cx="182" cy="271" r="132" fill="none" stroke="var(--navy)" stroke-width="1.5"/>
    </svg>
    <div class="badge-name">SHKA</div>

    <h1 class="headline headline--veteran">VETERAN</h1>
    <h1 class="headline headline--reserved">RESERVED</h1>
    <h1 class="headline headline--parking">PARKING</h1>

    <div class="web-band">
      <span class="web-band__address">SHKA.ORG</span>
    </div>

    <p class="thanks">THANK YOU FOR YOUR SERVICE</p>
  </main>
</body>
</html>
```